Business cards for the RT Group

We are looking for a template for our new business cards for our company that we can edit ourselves.
You will find our company colors in the logo. the logo on the back and on the front
first name Last Name
position
E-mail address
mobile number
landline number
Companies we have 2 RT Sicherheit GmbH and RT Services GmbH
address
Lindauer Weg 42
22543 Hamburg
www.rtverbund-beispiel.de

Something modern, simple but professional

if you have any questions, bring it on.

Industry/Entity Type

Sicherheit

Contact Information for Business Card

Steht in der Beschreibung

Colors
F0912C
F2A743
F7CA91
FBE8D2
FDF5EE

Requirements
Must have
• recognition value
Nice to have
• professional
Should not have
• Playful

```html
<!DOCTYPE html>
<html lang="de">
<head>
<meta charset="utf-8">
<title>RT Gruppe – Visitenkarten</title>
<link rel="stylesheet" href="https://fonts.googleapis.com/css2?family=Montserrat:wght@400;500;700;800&display=swap">
<style>
  :root{
    --stage:#8c8c8c;
    --orange:#f99a25;
    --orange-deep:#f0912c;
    --orange-text:#f07d14;
    --ink:#4a4a4a;
    --line:#1f1f1f;
    --paper:#ffffff;
  }
  *{box-sizing:border-box;margin:0;padding:0}
  html,body{width:1200px;height:1056px;overflow:hidden}
  body{background:var(--stage);font-family:"Montserrat",sans-serif;position:relative}
  .card{position:absolute;left:280px;width:640px;height:366px;box-shadow:0 14px 30px rgba(0,0,0,.28)}
  .card--front{top:90px;background:var(--orange);overflow:hidden}
  .card--back{top:580px;background:var(--paper)}

  .front__decoration{position:absolute;left:60px;top:30px;width:190px;height:336px;
    background:linear-gradient(180deg,#f68f1f 0%,#f48a1a 100%);opacity:.9;border-radius:40px 40px 0 0}
  .front__brand{position:absolute;left:280px;top:130px;color:var(--paper);font-weight:800;line-height:1}
  .front__brand-name{font-size:86px;letter-spacing:-2px}
  .front__brand-sub{font-size:28px;letter-spacing:6px;margin-top:6px;padding-left:4px}

  .back__brand{position:absolute;left:56px;top:50px;display:flex;align-items:center;gap:12px;color:var(--ink);font-weight:800}
  .back__brand-mark{width:22px;height:22px;background:var(--orange-deep)}
  .back__brand-name{font-size:40px;letter-spacing:-1px;line-height:1}
  .back__brand-sub{font-size:16px;letter-spacing:4px;margin-top:2px}

  .person{position:absolute;right:44px;top:58px;text-align:right}
  .person__name{color:var(--orange-text);font-weight:700;font-size:27px;letter-spacing:.5px}
  .person__role{color:var(--ink);font-size:15px;font-weight:500;margin-top:2px}

  .divider{position:absolute;left:88px;top:168px;width:370px;height:2px;background:var(--line)}
  .divider--accent{left:458px;width:138px;height:4px;top:166px;background:var(--orange-text)}

  .contact{list-style:none;position:absolute;font-size:14px;color:var(--ink);line-height:1.35}
  .contact li{display:flex;align-items:flex-start;gap:8px;margin-bottom:8px}
  .contact--right{right:44px;top:184px;text-align:right}
  .contact--right li{justify-content:flex-end}
  .contact--left{left:88px;top:240px}
  .icon{flex:none;width:18px;height:18px;border-radius:3px;background:var(--orange-deep);display:flex;align-items:center;justify-content:center;margin-top:1px}
  .icon svg{width:12px;height:12px;fill:var(--paper)}
</style>
</head>
<body>

<section class="card card--front" aria-label="Vorderseite">
  <div class="front__decoration" role="img" aria-label="Faint lantern silhouette decoration in a deeper orange tone"></div>
  <div class="front__brand">
    <div class="front__brand-name">RT</div>
    <div class="front__brand-sub">GRUPPE</div>
  </div>
</section>

<section class="card card--back" aria-label="Rückseite">
  <div class="back__brand">
    <span class="back__brand-mark"></span>
    <div>
      <div class="back__brand-name">RT</div>
      <div class="back__brand-sub">GRUPPE</div>
    </div>
  </div>

  <div class="person">
    <div class="person__name">LENA BERGER</div>
    <div class="person__role">Director / CEO</div>
  </div>

  <div class="divider"></div>
  <div class="divider divider--accent"></div>

  <ul class="contact contact--right">
    <li><span>www.rtverbund-beispiel.de</span>
      <span class="icon"><svg viewBox="0 0 12 12"><path d="M2 1l8 4-3.5 1L5 10z"/></svg></span></li>
    <li><span>Lindauer Weg 42<br>22543 Hamburg</span>
      <span class="icon"><svg viewBox="0 0 12 12"><path d="M6 0a4 4 0 0 1 4 4c0 3-4 8-4 8S2 7 2 4a4 4 0 0 1 4-4zm0 2.5a1.5 1.5 0 1 0 0 3 1.5 1.5 0 0 0 0-3z"/></svg></span></li>
  </ul>

  <ul class="contact contact--left">
    <li><span class="icon"><svg viewBox="0 0 12 12"><path d="M1 4c0-2 2-3 5-3s5 1 5 3H8V3H4v1zM3 5h6l2 5H1z"/></svg></span><span>(0)176-555018 42</span></li>
    <li><span class="icon"><svg viewBox="0 0 12 12"><path d="M3 1l2 2.5-1 1.5c.7 1.4 1.6 2.3 3 3l1.5-1L11 9l-1 2C5 11 1 7 1 2z"/></svg></span><span>040 555019</span></li>
    <li><span class="icon"><svg viewBox="0 0 12 12"><path d="M1 3h10v7H1zm1 1v.3l4 2.7 4-2.7V4z"/></svg></span><span>info@rtverbund-beispiel.com</span></li>
  </ul>
</section>

</body>
</html>
```